Kids sponsorship flyer to attract sponsorship and catch the eye

2 page flyer with pictures and text. Example in files. The flyer is for ....Corwin Baladez. Race number ...."811" 2 examples for were added now pictures and text (hand written added). Hoping for something clean that pops. Corwin is 7 years old. A mixture of images would be great
Target Market(s)
MX industry
Industry/Entity Type
Motocross industry
Colors
Designer to choose colors to be used in the design.
Requirements
Must have
- Name, number text and various images from supplied. Image on all 3 bikes and clear headshot without helmet.
Nice to have
- Multiple images...some cleaned up if possible.

```html
<!DOCTYPE html>
<html lang="en">
<head>
<meta charset="utf-8">
<title>Dex Harlan 22 – Sponsorship Flyer</title>
<link rel="stylesheet" href="https://fonts.googleapis.com/css2?family=Bebas+Neue&family=Poppins:wght@400;600&display=swap">
<style>
  :root {
    --stage: #1c1c1c;
    --ink: #111111;
    --panel: #1f1f1f;
    --steel: #6a6a6a;
    --rule: #b9b9b9;
    --gold-hi: #f3d67a;
    --gold-mid: #d3a43a;
    --gold-lo: #8a5a1c;
    --clay: #a8673f;
    --sky: #e9e6e1;
    --white: #ffffff;
  }
  * { margin: 0; padding: 0; box-sizing: border-box; }
  html, body { width: 1200px; height: 786px; overflow: hidden; background: var(--stage); }
  .stage { position: relative; width: 1200px; height: 786px; }

  .page { position: absolute; top: 73px; height: 639px; overflow: hidden; }
  .page--cover { left: 139px; width: 453px; background: var(--ink); }
  .page--story { left: 608px; width: 452px; background: var(--clay); }

  /* cover */
  .cover-photo { position: absolute; left: 0; top: 0; width: 453px; height: 578px;
    background: radial-gradient(ellipse at 35% 45%, #5b4a4a 0%, #7b5a44 35%, #a47455 70%, #8e6247 100%); }
  .cover-shapes { position: absolute; left: 0; top: 0; }
  .cover-name { position: absolute; left: 218px; top: 393px; width: 220px;
    font-family: "Bebas Neue", sans-serif; font-weight: 400; font-size: 64px; line-height: 0.9;
    white-space: nowrap; text-align: center;
    transform: scaleY(1.3); transform-origin: top center;
    background: linear-gradient(180deg, var(--gold-hi) 0%, var(--gold-mid) 45%, var(--gold-lo) 100%);
    -webkit-background-clip: text; background-clip: text; color: transparent; }
  .cover-rule { position: absolute; left: 0; top: 578px; width: 453px; height: 4px; background: var(--rule); }
  .sponsor-bar { position: absolute; left: 0; top: 582px; width: 453px; height: 57px; background: var(--ink);
    display: flex; align-items: center; padding: 0 16px; }
  .sponsors { display: flex; width: 256px; height: 30px; align-items: center; justify-content: space-between;
    background: #0a0a0a; padding: 0 10px; }
  .sponsor { font-family: "Poppins", sans-serif; font-weight: 600; font-size: 12px; color: var(--white); letter-spacing: 0.5px; }
  .sponsor-divider { width: 2px; height: 28px; background: var(--white); margin: 0 16px; }
  .socials { display: flex; gap: 10px; align-items: center; background: #0a0a0a; height: 22px; padding: 0 6px; }
  .social { display: flex; align-items: center; gap: 5px; font-family: "Poppins", sans-serif; font-size: 6px; color: var(--white); }
  .social-dot { width: 14px; height: 14px; border-radius: 3px; background: var(--white); }

  /* story */
  .story-hero { position: absolute; left: 0; top: 0; width: 452px; height: 460px;
    background: linear-gradient(180deg, var(--sky) 0%, #d6b89b 22%, #b37a52 55%, var(--clay) 100%); }
  .story-hero-subject { position: absolute; left: 200px; top: 0; width: 252px; height: 456px;
    background: radial-gradient(ellipse at 55% 55%, #6f6464 0%, #8c6a55 45%, rgba(168,103,63,0) 80%); }
  .story-intro, .story-lead, .story-body { position: absolute; font-family: "Poppins", sans-serif;
    font-size: 8.2px; line-height: 11px; text-align: justify; }
  .story-intro { left: 28px; top: 33px; width: 172px; color: var(--ink); }
  .story-thumb { position: absolute; left: 28px; width: 172px; border: 1.5px solid var(--white); }
  .story-thumb--corner { top: 131px; height: 118px; background: linear-gradient(160deg, #c59a78 0%, #6d5a57 50%, #9a6a4a 100%); }
  .story-thumb--gate { top: 257px; height: 118px; background: linear-gradient(180deg, #9aa0a2 0%, #7b6c66 45%, #6f5748 100%); }
  .story-name { position: absolute; left: 294px; top: 389px; font-family: "Bebas Neue", sans-serif; font-weight: 400;
    font-size: 36px; line-height: 0.9; white-space: nowrap; color: var(--white);
    transform: scaleY(1.25); transform-origin: top left; }
  .story-name-rule { position: absolute; left: 423px; top: 390px; width: 2px; height: 80px; background: var(--white); }
  .story-lead { left: 28px; top: 389px; width: 250px; color: var(--white); }
  .story-body { left: 28px; top: 480px; width: 397px; color: var(--white); }
</style>
</head>
<body>
<main class="stage">
  <section class="page page--cover">
    <div class="cover-photo" role="img" aria-label="Action photo of the young rider on his number 811 dirt bike on a dusty track"></div>
    <svg class="cover-shapes" width="453" height="578" viewBox="0 0 453 578" aria-hidden="true">
      <defs>
        <linearGradient id="goldStripe" x1="0" y1="1" x2="0" y2="0">
          <stop offset="0" stop-color="#8a5a1c"/><stop offset="0.6" stop-color="#d3a43a"/><stop offset="1" stop-color="#f3d67a"/>
        </linearGradient>
      </defs>
      <polygon points="416,0 453,0 453,578 119,578" fill="#1f1f1f" opacity="0.95"/>
      <polygon points="423,8 453,8 453,70 301,368 267,368" fill="#6a6a6a" opacity="0.8"/>
      <polygon points="288,235 302,235 160,497 143,497" fill="url(#goldStripe)"/>
    </svg>
    <h1 class="cover-name">Dex<br>Harlan 22</h1>
    <div class="cover-rule"></div>
    <footer class="sponsor-bar">
      <div class="sponsors">
        <span class="sponsor">Apex MX</span>
        <span class="sponsor">Ridgeline</span>
        <span class="sponsor">Greenline</span>
      </div>
      <span class="sponsor-divider"></span>
      <div class="socials">
        <span class="social"><span class="social-dot"></span>dexharlan_22</span>
        <span class="social"><span class="social-dot"></span>dexharlan_22</span>
      </div>
    </footer>
  </section>

  <section class="page page--story">
    <div class="story-hero" role="img" aria-label="Photo of the rider seated on his bike while a coach in a straw hat points out the track">
      <div class="story-hero-subject"></div>
    </div>
    <p class="story-intro">Lorem ipsum dolor sit amet, consectetuer adipiscing elit, sed diam nonummy nibh euismod tincidunt ut laoreet dolore magna aliquam erat vodolor sit amet, consectetuer adipiscing elit, sed diam nonummy nibh euismod tincidunt ut laoreet dolore magna volutpat. Ut wisi enim</p>
    <div class="story-thumb story-thumb--corner" role="img" aria-label="Rider leaning the 811 bike through a dirt corner"></div>
    <div class="story-thumb story-thumb--gate" role="img" aria-label="Young riders lined up at the starting gate"></div>
    <p class="story-lead">Lorem ipsum dolor sit amet, consectetuer adipiscing elit, sed diam nonummy nibh euismod tincidunt ut laoreet dolore magna aliquam erat volutpat. Ut wisi enim ad minim veniam, quis nostrud exerci tation ullamcorper suscipit lobortis nisl ut aliquip ex ea commodo Lorem ipsum dolor sit amet, consectetuer adipiscing elit, sed diam nonummy nibh euismod tincidunt ut laoreet dolore magna volutpat. Ut wisi enim</p>
    <h2 class="story-name">Dex<br>Harlan 22</h2>
    <span class="story-name-rule"></span>
    <p class="story-body">Lorem ipsum dolor sit amet, consectetuer adipiscing elit, sed diam nonummy nibh euismod tincidunt ut laoreet dolore magna aliquam erat volutpat. Ut wisi enim ad minim veniam, quis nostrud exerci tation ullamcorper suscipit lobortis nisl ut aliquip ex ea commodo consequat. Duis autem vel eum iriure dolor in hendrerit in vulputate velit esse molestie consequat, vel illum dolore eu Lorem ipsum dolor sit amet, consectetuer adipiscing elit, sed diam nonummy nibh euismod tincidunt ut laoreet dolore magna aliquam erat volutpat. Ut wisi enim ad minim veniam, quis nostrud exerci tation ullamcorper suscipit lobortis nisl ut aliquip ex ea commodo consequat. Lorem ipsum dolor sit amet, consectetuer adipiscing elit, sed diam nonummy nibh euismod tincidunt ut laoreet dolore magna aliquam erat volutpat. Ut wisi enim ad minim veniam, quis nostrud exerci tation ullamcorper suscipit lobortis nisl ut aliquip ex ea commodo consequat. Duis autem vel eum iriure dolor in hendrerit in vulputate velit ullamcorper suscipit lobortis nisl ut aliquip ex ea commodo consequat.</p>
  </section>
</main>
</body>
</html>
```